Copper Ridge Golf Circle Chart

I would like some type of design that can then be used on our website, like a png. or .jpeg or vector format. We want a circle/flow chart that describes our golf coaching process and has our logo faded in the background. attached is a rough draft to give you a general idea..something I created in word document but would like a much better version and attached is our logo. Our colors are red, black, and grey. The design does not necessarily have to have all of the bullet points..

Target Market(s)

Golfers, junior high golfers, high school golfers, adult golfers

Font styles to use
Sans Serif

Colors
ec1f27
f04a50
f59296
fbd4d5
aaaaaa
cbcbcb
1b1b1b
474747

Requirements
Nice to have
• Our colors are red, black, and grey, do not have to use all 3 in one design. Also The design does not necessarily have to have all of the bullet points.

```html
<!DOCTYPE html>
<html lang="en">
<head>
<meta charset="utf-8">
<title>Copper Ridge Golf – Coaching Process</title>
<link rel="stylesheet" href="https://fonts.googleapis.com/css2?family=Noto+Sans:wght@400;600&display=swap">
<style>
  :root {
    --red-strong: #ec1f27;
    --red-main: #f04a50;
    --red-soft: #f59296;
    --pink-pale: #fbd4d5;
    --pink-glow: #fdf0f0;
    --ink: #1b1b1b;
    --white: #ffffff;
  }
  html, body {
    margin: 0;
    padding: 0;
    width: 1200px;
    height: 1200px;
    overflow: hidden;
  }
  .canvas {
    width: 1200px;
    height: 1200px;
    background: radial-gradient(circle at 50% 50%, var(--pink-glow) 0%, var(--pink-pale) 72%);
    font-family: "Noto Sans", Verdana, sans-serif;
  }
  .process-wheel { display: block; }
  .segment--strong { fill: var(--red-main); }
  .segment--soft { fill: var(--red-soft); }
  .hub-ring { fill: var(--pink-glow); }
  .hub-disc { fill: var(--white); }
  .stage-title {
    fill: var(--white);
    font-size: 42px;
    font-weight: 400;
  }
  .stage-points {
    fill: var(--ink);
    font-size: 25px;
    font-weight: 400;
  }
  .stage-points--small { font-size: 22px; }
  .stage-points--large { font-size: 30px; }
  .brand-name {
    fill: var(--red-strong);
    font-size: 44px;
    font-weight: 600;
  }
</style>
</head>
<body>
<main class="canvas">
  <svg class="process-wheel" width="1200" height="1200" viewBox="0 0 1200 1200" role="img" aria-label="Copper Ridge Golf coaching process: Evaluation, Coaching, Practice, Measure Progress">
    <!-- Evaluation -->
    <path class="segment segment--strong" d="M157.9 506 A452 452 0 0 1 662.9 152.4 L681.5 273 L631 379.2 A223 223 0 0 0 381.9 553.6 L279.5 495.9 Z"/>
    <!-- Coaching -->
    <path class="segment segment--soft" d="M694 157.9 A452 452 0 0 1 1048.6 655.1 L928.4 675.8 L821.3 627.2 A223 223 0 0 0 646.4 381.9 L704.1 279.5 Z"/>
    <!-- Practice -->
    <path class="segment segment--strong" d="M1042.1 694 A452 452 0 0 1 537.1 1047.6 L518.5 927 L569 820.8 A223 223 0 0 0 818.1 646.4 L920.5 704.1 Z"/>
    <!-- Measure Progress -->
    <path class="segment segment--soft" d="M506 1042.1 A452 452 0 0 1 152.4 537.1 L273 518.5 L379.2 569 A223 223 0 0 0 553.6 818.1 L495.9 920.5 Z"/>

    <circle class="hub-ring" cx="600" cy="600" r="212"/>
    <circle class="hub-disc" cx="600" cy="600" r="196"/>
    <text class="brand-name" x="600" y="600" text-anchor="middle">
      <tspan x="600" dy="-38">Copper</tspan>
      <tspan x="600" dy="52">Ridge Golf</tspan>
    </text>

    <!-- Evaluation text -->
    <text class="stage-title" transform="translate(299 455) rotate(40)" text-anchor="middle">Evaluation</text>
    <text class="stage-points" transform="translate(318 349) rotate(-27)">
      <tspan x="0" dy="0">- video swing analysis</tspan>
      <tspan x="18" dy="33">- putting report</tspan>
      <tspan x="36" dy="33">- develop a plan</tspan>
    </text>

    <!-- Coaching text -->
    <text class="stage-title" transform="translate(780 320) rotate(-60)" text-anchor="middle">Coaching</text>
    <text class="stage-points stage-points--small" transform="translate(855 317) rotate(62)">
      <tspan x="0" dy="0">- tour quality technology</tspan>
      <tspan x="0" dy="29">- visualisation &amp; feedback</tspan>
      <tspan x="0" dy="29">- understand inconsistencies</tspan>
    </text>

    <!-- Practice text -->
    <text class="stage-title" transform="translate(880 770) rotate(38)" text-anchor="middle">Practice</text>
    <text class="stage-points" transform="translate(576 963) rotate(-27)">
      <tspan x="0" dy="0">- 24/7 Access to practice</tspan>
      <tspan x="10" dy="34">- practice with a purpose</tspan>
    </text>

    <!-- Measure Progress text -->
    <text class="stage-title" transform="translate(418 880) rotate(-60)" text-anchor="middle">
      <tspan x="0" dy="0">Measure</tspan>
      <tspan x="0" dy="44">Progress</tspan>
    </text>
    <text class="stage-points stage-points--large" transform="translate(258 618) rotate(62)">
      <tspan x="0" dy="0">track progress</tspan>
      <tspan x="0" dy="36">with data</tspan>
    </text>
  </svg>
</main>
</body>
</html>
```